Thank you for shopping with us business card

We would like a thank you card for our rebranded business. We used to be "Brindle Goods" but are now "Marlow Finds. Old thank you card and new logo will be attached for reference. New thank you card does not have to be same design as old thank you card, but please use new logo.
Shopmart URL is now marlowfinds.shopmart.example
Instagram is @Marlow_Finds
Email is marlowfinds@mailbox.example
Thank you!

Contact Information for Business Card

Shopmart site, email, Instagram

```html
<!DOCTYPE html>
<html lang="en">
<head>
<meta charset="utf-8">
<title>Marlow Finds – Thank You Card</title>
<link rel="stylesheet" href="https://fonts.googleapis.com/css2?family=Great+Vibes&family=Montserrat:wght@600&family=Roboto:wght@300;400&display=swap">
<style>
  :root {
    --page-bg: #f2f1f2;
    --card-light: #f68d3f;
    --card-dark: #ea7421;
    --ink: #111111;
  }
  * { margin: 0; padding: 0; box-sizing: border-box; }
  html, body {
    width: 1200px; height: 1200px; overflow: hidden;
    background: var(--page-bg);
  }
  .sheet { position: relative; width: 1200px; height: 1200px; }
  .card {
    position: absolute; left: 168px; width: 865px; height: 518px;
    background: radial-gradient(ellipse at 45% 40%, var(--card-light) 0%, var(--card-dark) 100%);
    box-shadow: 0 4px 14px rgba(0,0,0,0.25);
    color: var(--ink);
  }
  .card--front { top: 57px; }
  .card--back { top: 629px; }

  /* front */
  .brand-mark {
    position: absolute; left: 50%; top: 118px; width: 150px; height: 150px;
    transform: translateX(-50%); background: var(--ink);
  }
  .brand-name {
    position: absolute; left: 0; right: 0; top: 372px;
    text-align: center; font-family: "Montserrat", sans-serif; font-weight: 600;
    font-size: 35px; letter-spacing: 0.3px; text-transform: uppercase;
  }

  /* back */
  .thanks-title {
    position: absolute; left: 0; right: 0; top: 42px; text-align: center;
    font-family: "Great Vibes", cursive; font-size: 66px; line-height: 1;
  }
  .thanks-message {
    position: absolute; left: 0; right: 0; top: 146px; text-align: center;
    font-family: "Roboto", sans-serif; font-weight: 300; font-size: 26px; line-height: 38.5px;
  }
  .contact-list {
    position: absolute; left: 62px; top: 352px; list-style: none;
    font-family: "Roboto", sans-serif; font-weight: 400; font-size: 21px;
  }
  .contact-item { display: flex; align-items: center; height: 38.5px; }
  .contact-icon {
    width: 27px; height: 27px; border-radius: 50%; background: var(--ink);
    margin-right: 11px; flex: none; display: flex; align-items: center; justify-content: center;
  }
  .corner-brand {
    position: absolute; right: 62px; bottom: 58px; text-align: center;
    font-family: "Montserrat", sans-serif; font-weight: 600; font-size: 15px;
    text-transform: uppercase;
  }
  .corner-brand__mark { width: 62px; height: 62px; background: var(--ink); margin: 0 auto 8px; }
</style>
</head>
<body>
<main class="sheet">
  <section class="card card--front" aria-label="Card front">
    <div class="brand-mark"></div>
    <h1 class="brand-name">Marlow Finds</h1>
  </section>

  <section class="card card--back" aria-label="Card back">
    <h2 class="thanks-title">Thank You For Your Purchase</h2>
    <p class="thanks-message">Your purchase made my day and I hope<br>this package brightens yours.<br>Please come back and leave a review!</p>
    <ul class="contact-list">
      <li class="contact-item"><span class="contact-icon"></span>marlowfinds.shopmart.example</li>
      <li class="contact-item">
        <span class="contact-icon">
          <svg width="17" height="13" viewBox="0 0 17 13" aria-hidden="true">
            <rect x="1" y="1" width="15" height="11" fill="none" stroke="#f68d3f" stroke-width="1.4"/>
            <path d="M1 1 L8.5 7 L16 1 M1 12 L6.5 6 M16 12 L10.5 6" fill="none" stroke="#f68d3f" stroke-width="1.4"/>
          </svg>
        </span>marlowfinds@mailbox.example</li>
      <li class="contact-item"><span class="contact-icon"></span>@Marlow_Finds</li>
    </ul>
    <div class="corner-brand">
      <div class="corner-brand__mark"></div>
      Marlow Finds
    </div>
  </section>
</main>
</body>
</html>
```